Vitamin B12 Liquid Drops Label

hi, i need a label designed for my vitamin b12 drops that i am going to be selling on bazaroo. the label needs to quickly capture the attention of a buyer as he or she is scrolling through the thumbnail search results on bazaroo.example my brand is called zulpa. i already have an example brand logo i will be using, however, i need help designing the rest of the label. attached are some examples of labels i like for other supplements.some of these examples are pink. i do not want pink. please go for a blue/green color scheme. THE DESIGN MUST BE BOLD

Target Market(s)

adults ages 30 - 64

Font styles to use
Sans Serif

Colors
0455a3
cedeed
3176b5
85acd3
cfdeed
9bcb3b
abd037
cadf82
00a990

Requirements
Must have
• - bold design
• - somewhat gender-neutral color scheme because this will be used equally by men and women
• - B12 MUST be very prominent and visible on the label
Should not have
• - it should not be "crunchy" looking

```html
<!DOCTYPE html>
<html lang="en">
<head>
<meta charset="utf-8">
<title>Zulpa Vitamin B12 Label</title>
<link href="https://fonts.googleapis.com/css2?family=Archivo+Black&family=Oswald:wght@500;700&family=Roboto:ital,wght@0,300;0,400;0,500;0,700;1,400;1,700;1,900&display=swap" rel="stylesheet">
<style>
  :root{
    --lime:#c9dd8a;
    --lime-deep:#abd037;
    --teal:#1fa68f;
    --teal-dark:#00a990;
    --ink:#111111;
    --blue:#0455a3;
    --silver:#c9ced3;
    --white:#ffffff;
    --page:#ffffff;
  }
  *{box-sizing:border-box;margin:0;padding:0}
  html,body{width:1200px;height:1200px;overflow:hidden;background:var(--page)}
  body{font-family:'Roboto',sans-serif;color:var(--ink);position:relative}

  .label{position:absolute;left:40px;top:390px;width:1120px;height:420px;overflow:hidden;background:var(--lime)}
  .band-green{position:absolute;left:0;top:0;width:100%;height:240px;background:var(--lime)}
  .band-silver{position:absolute;left:0;top:240px;width:100%;height:10px;background:linear-gradient(#eef0f2,var(--silver))}
  .band-teal{position:absolute;left:0;top:250px;width:100%;height:120px;background:var(--teal)}
  .band-black{position:absolute;left:0;top:370px;width:100%;height:34px;background:var(--ink)}
  .band-teal-foot{position:absolute;left:0;top:404px;width:100%;height:16px;background:var(--teal)}

  /* left panel */
  .panel-left{position:absolute;left:20px;top:22px;width:330px;font-size:11px;line-height:1.3;text-align:justify}
  .panel-left p{margin-bottom:8px}
  .panel-left .caps{text-transform:uppercase;font-weight:500;font-size:10.5px;margin-bottom:0;text-align:left}
  .disclaimer{border:1px solid var(--ink);padding:3px 5px;font-style:italic;font-size:8.5px;margin-top:6px}
  .left-claims{position:absolute;left:20px;top:268px;width:330px;color:var(--white);font-size:13px;line-height:1.4}
  .left-claims .big{font-family:'Oswald',sans-serif;font-size:34px;float:left;line-height:1;margin-right:6px}
  .left-claims .lot{clear:both;padding-top:14px;font-size:12px}

  /* front */
  .brand{position:absolute;left:378px;top:26px;width:400px;text-align:center;font-family:'Archivo Black',sans-serif;font-size:44px;letter-spacing:1px}
  .vitamin-vert{position:absolute;left:368px;top:96px;width:130px;height:40px;transform-origin:left top;transform:translate(0,130px) rotate(-90deg);font-family:'Oswald',sans-serif;font-weight:700;color:var(--blue);font-size:34px;letter-spacing:1px;line-height:40px}
  .b12{position:absolute;left:412px;top:66px;font-family:'Oswald',sans-serif;font-weight:700;line-height:1;white-space:nowrap}
  .b12 .b{font-size:158px;letter-spacing:-2px}
  .b12 .num{font-size:112px;font-weight:500;vertical-align:top;display:inline-block;margin-top:8px}
  .slant{position:absolute;left:0;top:0}
  .dietary{position:absolute;left:560px;top:196px;color:var(--white);font-style:italic;font-weight:400;font-size:27px;letter-spacing:.3px;white-space:nowrap}
  .benefits{position:absolute;left:420px;top:262px;width:320px;color:var(--white);font-size:17px;font-weight:300;list-style:none;line-height:1.3}
  .benefits li{position:relative;padding-left:22px;margin-bottom:8px}
  .benefits svg{position:absolute;left:0;top:2px}
  .count{position:absolute;left:520px;top:371px;color:var(--white);font-style:italic;font-weight:900;font-size:25px}

  /* right panel */
  .badges{position:absolute;left:812px;top:24px;display:flex;flex-direction:column;gap:10px}
  .badge{width:46px;height:46px;border-radius:50%;border:3px solid var(--ink);background:var(--lime-deep)}
  .info-column{position:absolute;left:880px;top:18px;width:226px;height:352px;display:flex;flex-direction:column;gap:6px}
  .facts{background:var(--white);border:1px solid var(--ink);padding:5px 7px;font-size:8px;line-height:1.25}
  .facts h3{font-family:'Roboto',sans-serif;font-weight:700;font-size:17px;line-height:1.1}
  .facts .meta{font-size:7.5px;border-bottom:5px solid var(--ink);padding-bottom:3px}
  .facts .amount{text-align:right;font-weight:700;border-bottom:2px solid var(--ink);padding:2px 0;font-size:7.5px}
  .facts table{width:100%;border-collapse:collapse;font-size:7.5px}
  .facts td{padding:0}
  .facts td.v{text-align:right;white-space:nowrap}
  .facts tr.rule td{border-top:1px solid var(--ink)}
  .facts .dv{border-top:2px solid var(--ink);padding-top:2px;font-size:7.5px}
  .facts .other{border:1px solid var(--ink);margin-top:5px;padding:2px 3px;font-size:7.5px}
  .contact{flex:1;background:var(--white);text-align:center;padding-top:6px}
  .contact .q{background:var(--teal);color:var(--white);font-size:10px;padding:3px 0}
  .contact .help{font-size:9.5px;margin-top:4px}
  .contact .mail{font-size:15px;color:var(--teal-dark);font-weight:500;margin-top:4px}
  .seal-usa{position:absolute;left:820px;top:268px;width:44px;height:44px;border-radius:50%;background:var(--blue);border:3px solid var(--white)}
  .seal-reg{position:absolute;left:820px;top:326px;width:46px;height:22px;border:2px solid var(--white);border-radius:3px}
</style>
</head>
<body>
<main class="label">
  <div class="band-green"></div>
  <div class="band-silver"></div>
  <div class="band-teal"></div>
  <div class="band-black"></div>
  <div class="band-teal-foot"></div>

  <section class="panel-left">
    <p><b>SUGGESTED USE:</b> As dietary supplement take one capsule twice a day. For best results take 20–30 min before a meal or as directed by your healthcare professional.</p>
    <p><b>CAUTION:</b> Do not exceed recommended dose. Pregnant or nursing mothers, children under the age of 18, and individuals with a known medical condition should consult a physician before using this or any dietary supplement.</p>
    <p class="caps">Keep out of reach of children</p>
    <p class="caps">Do not use if safety seals damaged or missing</p>
    <p class="caps">Store in a cool, dry place</p>
    <p class="disclaimer">These statements have not been evaluated by the Food and Drug Administration. This product is not intended to diagnose, treat, cure or prevent any disease.</p>
  </section>
  <section class="left-claims">
    <span class="big">NO</span>Artificial Ingredients, Antibiotics, Hormones, Sugar or Preservatives.
    <div class="lot">Lot and Expiration Date Printed on bottom of bottle</div>
  </section>

  <svg class="slant" width="1120" height="420" aria-hidden="true">
    <polygon points="530,190 860,190 860,230 505,230" fill="#111"/>
    <polygon points="505,230 860,230 860,240 498,240" fill="#c9ced3"/>
    <polygon points="500,370 730,370 712,404 482,404" fill="#111"/>
  </svg>

  <div class="brand">ZULPA</div>
  <div class="vitamin-vert">VITAMIN</div>
  <h1 class="b12"><span class="b">B</span><span class="num">12</span></h1>
  <div class="dietary">Dietary supplement</div>

  <ul class="benefits">
    <li><svg width="16" height="16" viewBox="0 0 16 16"><path d="M1 9l4 4 10-12" stroke="#fff" stroke-width="3" fill="none"/></svg>Helps support a healthy nervous system and energy production</li>
    <li><svg width="16" height="16" viewBox="0 0 16 16"><path d="M1 9l4 4 10-12" stroke="#fff" stroke-width="3" fill="none"/></svg>Supports healthy brain function</li>
  </ul>
  <div class="count">250 Tablets</div>

  <div class="badges">
    <div class="badge"></div>
    <div class="badge"></div>
    <div class="badge"></div>
  </div>

  <div class="seal-usa"></div>
  <div class="seal-reg"></div>

  <div class="info-column">
    <section class="facts">
      <h3>Supplement Facts</h3>
      <div class="meta"><b>Serving Size:</b> 1 Veggie Capsule<br><b>Servings Per Container:</b> 60</div>
      <div class="amount">Amount Per Serving %DV</div>
      <table>
        <tr><td>Enzora-Plex™</td><td class="v">2500HUT/400 mg</td></tr>
        <tr><td>Enzyme Blend:</td><td></td></tr>
        <tr><td>Fungal Protease from Aspergillus oryzae</td><td></td></tr>
        <tr><td>Lactobacillus acidophilus</td><td></td></tr>
        <tr><td>Lactobacillus casei</td><td></td></tr>
        <tr><td>Lactobacillus plantarum</td><td></td></tr>
        <tr class="rule"><td>Bromelain</td><td class="v">90 GDU</td></tr>
        <tr class="rule"><td>Papain</td><td class="v">2670 TU</td></tr>
        <tr class="rule"><td>Fungal Lipase</td><td class="v">1500 FIP</td></tr>
        <tr class="rule"><td>Fungal Lactase</td><td class="v">600 LACU</td></tr>
        <tr class="rule"><td>Alpha Galactosidase</td><td class="v">300 GALU</td></tr>
      </table>
      <div class="dv">** Daily Value (DV) not established</div>
      <div class="other">Other Ingredients: Cellulose (Vegetable Capsule), Vegetable Magnesium Stearate, Silicon Dioxide.</div>
    </section>
    <section class="contact">
      <div class="q">Questions about our product?</div>
      <div class="help">We are here to help you! Email our team</div>
      <div class="mail">help@zulpa.example</div>
    </section>
  </div>
</main>
</body>
</html>
```